Business Card cabinets and cabinets components making company.

the card should be formal and interesting at the same time. The main colors will be black and white.

Font styles to use
Sans Serif

Colors

Designer to choose only greyscale colors for use in the design.

Requirements
Must have
• At least must have the followings:
office phone
cell phone
address
position
name
email
web

```html
<!DOCTYPE html>
<html lang="en">
<head>
<meta charset="utf-8">
<title>Joinwell business card</title>
<link href="https://fonts.googleapis.com/css2?family=Roboto:wght@400;500;700&display=swap" rel="stylesheet">
<style>
  :root {
    --backdrop: #b8b8b8;
    --paper: #ffffff;
    --ink: #1c1c1c;
    --panel: #2a2a2a;
    --card-dark: #1e1e1e;
    --brand-light: #d6d6d6;
  }
  * { margin: 0; padding: 0; box-sizing: border-box; }
  html, body { width: 1200px; height: 801px; overflow: hidden; }
  body {
    background: var(--backdrop);
    font-family: "Roboto", Arial, sans-serif;
    color: var(--ink);
    position: relative;
  }
  .card {
    position: absolute;
    top: 274px;
    width: 443px;
    height: 263px;
    overflow: hidden;
  }
  .card-front { left: 153px; background: var(--paper); }
  .card-back { left: 625px; background: var(--card-dark); }

  .front-band {
    position: absolute;
    top: 0;
    left: 258px;
    width: 152px;
    height: 100%;
    background: var(--panel);
  }
  .person { position: absolute; left: 38px; top: 48px; }
  .person-name {
    font-weight: 500;
    font-size: 16px;
    letter-spacing: 0.2px;
    line-height: 18px;
  }
  .person-role { font-size: 12px; line-height: 14px; }

  .contacts {
    position: absolute;
    left: 38px;
    top: 100px;
    list-style: none;
    font-size: 12.5px;
    line-height: 15.6px;
  }
  .contacts li { display: flex; align-items: center; gap: 5px; }
  .contacts svg { width: 11px; height: 11px; flex: none; }

  .address {
    position: absolute;
    left: 38px;
    top: 181px;
    font-size: 12.5px;
    line-height: 15.6px;
    font-style: normal;
  }

  .brand-name {
    position: absolute;
    left: 0;
    right: 0;
    top: 105px;
    text-align: center;
    font-weight: 500;
    font-size: 48px;
    line-height: 52px;
    color: var(--brand-light);
  }
</style>
</head>
<body>
  <section class="card card-front">
    <div class="front-band"></div>
    <div class="person">
      <div class="person-name">DANIEL HARTLEY</div>
      <div class="person-role">Managing Director</div>
    </div>
    <ul class="contacts">
      <li>
        <svg viewBox="0 0 12 12" fill="none" stroke="#1c1c1c" stroke-width="1.5"><path d="M2 1.5l2 0 1 2.5-1.3 1a6 6 0 0 0 3.3 3.3l1-1.3 2.5 1v2A1 1 0 0 1 9.5 11 8.5 8.5 0 0 1 1 2.5 1 1 0 0 1 2 1.5z"/></svg>
        044-210 555 014
      </li>
      <li>
        <svg viewBox="0 0 12 12" fill="none" stroke="#1c1c1c" stroke-width="1.4"><rect x="3" y="0.8" width="6" height="10.4" rx="1"/><line x1="5.3" y1="9.3" x2="6.7" y2="9.3"/></svg>
        044-210 555 014
      </li>
      <li>
        <svg viewBox="0 0 12 12"><rect x="0.5" y="2.5" width="11" height="7" fill="#1c1c1c"/><path d="M0.8 3l5.2 3.6L11.2 3" fill="none" stroke="#fff" stroke-width="1"/></svg>
        info@joinwell.com
      </li>
      <li>
        <svg viewBox="0 0 12 12" fill="none" stroke="#1c1c1c" stroke-width="1.1"><circle cx="6" cy="6" r="5"/><ellipse cx="6" cy="6" rx="2.2" ry="5"/><line x1="1" y1="6" x2="11" y2="6"/></svg>
        www.joinwell.com
      </li>
    </ul>
    <address class="address">421, Address line goes here<br>45452,Country Name</address>
  </section>

  <section class="card card-back">
    <div class="brand-name">Joinwell</div>
  </section>
</body>
</html>
```